Professional and modern website for Real Estate services company

Hi there! We're looking for a responsive, highly professional and modern (in line with Latest trends) coded website for a Real Estate services company named Brightmere (find logo attached). I will try to Explain how I picture it in my head, but feel free to step out of the script and design it as you please. The structure for the website must be as Follows: - Menu: at the top of the screen, always visible (in any page and when to scrolling down). Logo at the left hand side (clicking redirects to home), then a Services, About us, Blog and Contact and on the right hand, Estimate and Log in (just placeholder, no log in required yet). - Home: (I like https://fr.velmora.example/): a landscape picture of Madrid's skyline. Very important That at a first glance (without scrolling) you can see a box to input data of your building to get an estimate (Post code, Number of homes, Number of garages, Number of stores, Swimming pool (yes / no) Concierge (yes / no)). Should there be a small space Also for a corporate presentation video (more or less like https://www.bravunecasales.example/ but With the estimate Request box INSTEAD OF the App - however, do not take this one as example Given I just wanted to illustrate the structure). Still in the Home, bellow the first glance, I'd like to have a brief introduction of the following pages (Services, About us, Blog and Contact). This can be in a Either "square" form (like https://fr.velmora.example/) or in a "scroll" form (like https://k7portales.example/). - Services: we offer 3 sets of services, each of them composed by three specific services, Namely: * Administration Treasury Accounting Savings * Consulting Legal Technical Regulatory * Mediation Repairs Meetings Delinquency For the sake of structuring, each of the nine services will Have to written description composed of 3 small paragraphs of About 15 words. I Tend to like to Accompany With each of the services related icons / vectors, but feel free to design them as you want. - About us: content not yet defined, but will be a series of bullets / sections in Which We talk about prep or differentiating points. We can include the corporate video presentation here again. - Blog: just a space Where you can see to the blog entries (in Home, probably just show 3/4). - Contact: a fancy contact form, with map, address, telephone, e-mail and opening hours. Just to give it a bit more content, maybe include a catch phrase like "We're looking forward to meeting you!" or something like that. - Estimate: this is the Most Important page in the website (in Addition to the upper part of the Home page). Basically replicate the estimate for the home box, but maybe with a bit more design or extended, Given this is a single page just for that. - Log in: opens a drop-down with user and password (just placeholder, no log in required yet). Regarding colors, we still do not Have a color scheme, so anything in line With the logo is OK. Many thanks in advance, Martin

Target Market(s)

All ages and genders

Industry/Entity Type

Real Estate

Coding

Coded - Design and coding required

Number of Pages Required

5+ page

Font styles to use
Sans Serif

Requirements
Must have
• Blank colored background

```html
<!DOCTYPE html>
<html lang="en">
<head>
<meta charset="utf-8">
<title>Brightmere — Real Estate Services</title>
<link rel="stylesheet" href="https://fonts.googleapis.com/css2?family=Roboto+Condensed:wght@400;700&family=Open+Sans:wght@400;600;700&display=swap">
<style>
:root{
  --orange:#c8620f;
  --brown:#6b3a14;
  --ink:#333333;
  --line:#d9d9d9;
  --white:#ffffff;
  --blog-deep:#a0614a;
  --blog-soft:#b58a78;
  --footer:#343434;
  --footer-field:#262626;
  --bottom:#262626;
}
*{box-sizing:border-box;margin:0;padding:0}
html,body{width:1200px;height:2679px;overflow:hidden}
body{position:relative;background:#fff;font-family:"Open Sans",Arial,sans-serif;color:var(--ink)}
.abs{position:absolute}
.head{font-family:"Roboto Condensed","Arial Narrow",sans-serif;font-weight:700;text-transform:uppercase}

.site-nav{left:0;top:0;width:1200px;height:60px;background:rgba(255,255,255,.96);z-index:5;border-bottom:1px solid #eee}
.brand{left:161px;top:13px;display:flex;align-items:center;gap:8px;font-family:"Open Sans",sans-serif;font-weight:700;font-size:26px;color:#3c3c3c;letter-spacing:-.5px}
.brand-dot{width:12px;height:12px;background:var(--orange)}
.menu{right:160px;top:22px;display:flex;gap:22px;font-family:"Roboto Condensed",sans-serif;font-size:12px;text-transform:uppercase;color:#444}
.menu .active{color:var(--orange);position:relative}
.menu .active::after{content:"";position:absolute;left:0;right:0;bottom:-7px;margin:auto;width:14px;height:2px;background:var(--orange)}

.hero{left:0;top:60px;width:1200px;height:480px;background:linear-gradient(100deg,#4a2f1c 0%,#7a5234 35%,#a0784f 60%,#5e3d24 100%)}
.hero-shade{left:0;top:60px;width:1200px;height:480px;background:rgba(0,0,0,.18)}
.hero-title{left:0;width:1200px;top:186px;text-align:center;color:#fff;font-size:46px;letter-spacing:.5px}
.hero-rule{left:556px;top:240px;width:88px;height:2px;background:#fff}
.hero-sub{left:0;width:1200px;top:265px;text-align:center;color:#fff;font-size:12px;line-height:18px;text-transform:uppercase}
.btn{display:block;background:var(--orange);color:#fff;border-radius:14px;text-align:center;font-family:"Roboto Condensed",sans-serif;text-transform:uppercase}
.hero-btn{left:547px;top:321px;width:107px;height:26px;line-height:26px;font-size:11px}
.slider-dots{left:1168px;top:283px;display:flex;flex-direction:column;gap:6px}
.slider-dots i{display:block;width:10px;height:10px;border-radius:50%;border:1px solid var(--orange)}
.slider-dots i.on{background:var(--orange)}

.est-tab{left:161px;top:452px;width:127px;height:28px;background:var(--orange);color:#fff;font-size:14px;padding:8px 0 0 33px;border-radius:6px 6px 0 0}
.est-box{left:161px;top:479px;width:879px;height:119px;background:var(--orange);border-radius:0 6px 6px 6px}
.field{height:29px;background:#fff;border-radius:3px;font-size:10px;color:#555;padding:9px 6px;text-transform:uppercase}
.submit{left:875px;top:523px;width:129px;height:32px;line-height:32px;background:var(--brown);font-size:11px;border-radius:16px}

.sec-title{left:0;width:1200px;text-align:center;font-size:24px;color:#333}
.sec-title span,.about-title span{color:var(--orange)}
.sec-rule{width:18px;height:2px;background:#333}

.about-title{left:161px;top:680px;font-size:24px}
.about-text{left:161px;top:740px;width:425px;font-size:12px;line-height:16px;color:#444}
.about-text p+p{margin-top:16px}
.video{left:611px;top:648px;width:429px;height:249px;background:linear-gradient(180deg,#596872 0%,#8e979d 40%,#3e4346 100%)}
.video-bar{left:611px;top:856px;width:429px;height:41px;background:rgba(0,0,0,.55)}
.play{left:620px;top:862px;width:50px;height:28px;background:#2a2a2a;border-radius:3px}
.progress{left:690px;top:874px;width:260px;height:5px;background:#1a8bd6}

.svc-icon{width:59px;height:59px;border:1px solid var(--line);background:#fff;display:flex;align-items:center;justify-content:center}
.svc-icon.on{background:var(--orange);border-color:var(--orange)}
.svc-name{font-family:"Roboto Condensed",sans-serif;font-weight:700;font-size:13px;color:#333;text-transform:uppercase}
.svc-name.on{color:var(--orange)}
.svc-text{font-size:11px;line-height:13px;color:#555;width:200px}

.blog-date{font-family:"Roboto Condensed",sans-serif;font-weight:700;font-size:10px}
.blog-title{font-size:25px;line-height:28px}
.blog-text{font-size:10px;line-height:16px;text-transform:uppercase;font-weight:600}
.blog-btn{width:81px;height:22px;line-height:22px;background:#fff;color:var(--orange);font-size:10px;border-radius:11px}

.map{left:0;top:2000px;width:1200px;height:268px;background:linear-gradient(120deg,#e6d6b8 0%,#d9c6a2 50%,#e9dcc1 100%)}
.map-pop{left:479px;top:2057px;width:243px;height:104px;background:#fff;border-radius:6px;box-shadow:0 2px 10px rgba(0,0,0,.25);text-align:center;padding-top:34px;font-family:"Roboto Condensed",sans-serif;font-weight:700;font-size:14px;line-height:18px;color:#333}
.map-tip{left:588px;top:2160px;width:0;height:0;border-left:12px solid transparent;border-right:12px solid transparent;border-top:14px solid #fff}

.footer{left:0;top:2268px;width:1200px;height:361px;background:var(--footer)}
.foot-title{font-size:17px;color:#fff}
.foot-rule{width:18px;height:2px;background:var(--orange)}
.foot-line{color:#fff;font-size:11px;line-height:16px}
.info{display:flex;align-items:center;gap:16px;color:#fff;font-size:11px}
.info svg{width:14px;height:14px}
.ffield{background:var(--footer-field);color:#fff;font-size:10px;padding:10px 8px;text-transform:uppercase}
.send{left:461px;top:2534px;width:94px;height:29px;line-height:29px;font-size:12px;border-radius:15px}
.bottom{left:0;top:2629px;width:1200px;height:50px;background:var(--bottom);color:#fff;font-size:10px;text-align:center;line-height:50px;font-weight:600}
</style>
</head>
<body>

<header class="abs site-nav">
  <div class="abs brand"><span>Brightmere</span><span class="brand-dot"></span></div>
  <nav class="abs menu">
    <span class="active">Home</span><span>Services</span><span>About Us</span><span>Blog</span><span>Contact</span><span>Estimate</span><span>Login</span>
  </nav>
</header>

<div class="abs hero" role="img" aria-label="Photo of a warm, modern hotel-style bedroom with sofa and city view"></div>
<div class="abs hero-shade"></div>
<h1 class="abs head hero-title">Build Your Dream</h1>
<div class="abs hero-rule"></div>
<p class="abs hero-sub">Lorem ipsum dolor sit amet, consectetur adipisicing elit, sed do eiusmod<br>tempor incididunt ut labore et dolore magna aliqua.</p>
<a class="abs btn hero-btn">Learn More</a>
<div class="abs slider-dots"><i></i><i class="on"></i><i></i></div>

<div class="abs head est-tab">Estimate</div>
<div class="abs est-box"></div>
<div class="abs field" style="left:177px;top:500px;width:211px">Post Code</div>
<div class="abs field" style="left:398px;top:500px;width:211px">Number of Homes</div>
<div class="abs field" style="left:618px;top:500px;width:211px">Number of Garages</div>
<div class="abs field" style="left:177px;top:548px;width:211px">Number of Stores</div>
<div class="abs field" style="left:398px;top:548px;width:211px">Swimming Pool</div>
<div class="abs field" style="left:618px;top:548px;width:211px">Concierge</div>
<a class="abs btn submit">Submit</a>

<h2 class="abs head about-title">About <span>Us</span></h2>
<div class="abs sec-rule" style="left:161px;top:716px"></div>
<div class="abs about-text">
  <p>Lorem ipsum dolor sit amet, consectetur adipisicing elit, sed do eiusmod tempor incididunt ut labore et dolore magna aliqua. Ut enim ad minim veniam. quis nostrud exercitation ullamco.</p>
  <p>Laboris nisi ut aliquip ex ea commodo consequat. Duis aute irure dolor in reprehen-derit in voluptate velit esse cillum dolore.eu fugiat nulla pariatur. Excepteur sint occaecat cupidatat non proident, sunt in culpa.</p>
</div>
<div class="abs video" role="img" aria-label="Corporate presentation video still: a white citadel on a misty mountain"></div>
<div class="abs video-bar"></div>
<div class="abs play"><svg width="50" height="28"><path d="M21 9 L31 14 L21 19 Z" fill="#fff"/></svg></div>
<div class="abs progress"></div>

<h2 class="abs head sec-title" style="top:950px">Our <span>Services</span></h2>
<div class="abs sec-rule" style="left:591px;top:985px"></div>

<div class="abs svc-icon on" style="left:161px;top:1014px"><svg width="30" height="30" viewBox="0 0 30 30" fill="#fff"><path d="M15 3 L28 10 H2 Z"/><rect x="5" y="12" width="3" height="11"/><rect x="11" y="12" width="3" height="11"/><rect x="16" y="12" width="3" height="11"/><rect x="22" y="12" width="3" height="11"/><rect x="2" y="24" width="26" height="3"/></svg></div>
<div class="abs svc-name on" style="left:234px;top:1014px">Treasury</div>
<div class="abs svc-text" style="left:234px;top:1032px">There are many variations of demo text passed sages of Lorem Ipsum available but the majority.</div>

<div class="abs svc-icon" style="left:461px;top:1014px"><svg width="30" height="30" viewBox="0 0 30 30" fill="none" stroke="#333" stroke-width="2"><rect x="6" y="3" width="18" height="24" rx="2"/><path d="M15 9v12M18 11h-4a2 2 0 0 0 0 4h2a2 2 0 0 1 0 4h-4"/></svg></div>
<div class="abs svc-name" style="left:534px;top:1014px">Accounting</div>
<div class="abs svc-text" style="left:534px;top:1032px">There are many variations of demo text passed sages of Lorem Ipsum available but the majority.</div>

<div class="abs svc-icon" style="left:761px;top:1014px"><svg width="30" height="30" viewBox="0 0 30 30" fill="none" stroke="#333" stroke-width="2"><circle cx="17" cy="10" r="7"/><path d="M17 6v8"/><path d="M3 22h6l5 3 9-4"/></svg></div>
<div class="abs svc-name" style="left:834px;top:1014px">Savings</div>
<div class="abs svc-text" style="left:834px;top:1032px">There are many variations of demo text passed sages of Lorem Ipsum available but the majority.</div>

<div class="abs svc-icon" style="left:161px;top:1122px"><svg width="30" height="30" viewBox="0 0 30 30" fill="none" stroke="#333" stroke-width="2"><path d="M15 4v22M8 26h14M5 8h20M5 8l-3 8h6zM25 8l-3 8h6z"/></svg></div>
<div class="abs svc-name" style="left:234px;top:1122px">Legal</div>
<div class="abs svc-text" style="left:234px;top:1140px">There are many variations of demo text passed sages of Lorem Ipsum available but the majority.</div>

<div class="abs svc-icon" style="left:461px;top:1122px"><svg width="30" height="30" viewBox="0 0 30 30" fill="none" stroke="#333" stroke-width="3"><circle cx="15" cy="15" r="6"/><path d="M15 2v5M15 23v5M2 15h5M23 15h5M6 6l3.5 3.5M20.5 20.5L24 24M6 24l3.5-3.5M20.5 9.5L24 6"/></svg></div>
<div class="abs svc-name" style="left:534px;top:1122px">Technical</div>
<div class="abs svc-text" style="left:534px;top:1140px">There are many variations of demo text passed sages of Lorem Ipsum available but the majority.</div>

<div class="abs svc-icon" style="left:761px;top:1122px"><svg width="30" height="30" viewBox="0 0 30 30" fill="none" stroke="#333" stroke-width="2"><rect x="5" y="5" width="18" height="22" rx="2"/><rect x="10" y="3" width="8" height="4"/><path d="M9 13h10M9 18h6"/><path d="M19 22l2 2 4-4"/></svg></div>
<div class="abs svc-name" style="left:834px;top:1122px">Regulatory</div>
<div class="abs svc-text" style="left:834px;top:1140px">There are many variations of demo text passed sages of Lorem Ipsum available but the majority.</div>

<div class="abs svc-icon" style="left:161px;top:1232px"><svg width="30" height="30" viewBox="0 0 30 30" fill="none" stroke="#333" stroke-width="3"><path d="M5 5l20 20M25 5L5 25"/></svg></div>
<div class="abs svc-name" style="left:234px;top:1232px">Repairs</div>
<div class="abs svc-text" style="left:234px;top:1250px">There are many variations of demo text passed sages of Lorem Ipsum available but the majority.</div>

<div class="abs svc-icon" style="left:461px;top:1232px"><svg width="30" height="30" viewBox="0 0 30 30" fill="none" stroke="#333" stroke-width="2"><circle cx="9" cy="7" r="3"/><circle cx="21" cy="7" r="3"/><path d="M4 26V14h10v12M16 26V14h10v12"/></svg></div>
<div class="abs svc-name" style="left:534px;top:1232px">Meetings</div>
<div class="abs svc-text" style="left:534px;top:1250px">There are many variations of demo text passed sages of Lorem Ipsum available but the majority.</div>

<div class="abs svc-icon" style="left:761px;top:1232px"><svg width="30" height="30" viewBox="0 0 30 30" fill="none" stroke="#333" stroke-width="2"><path d="M7 4h12l5 5v17H7z"/><path d="M11 12h9M11 16h9M11 20h6"/></svg></div>
<div class="abs svc-name" style="left:834px;top:1232px">Delinquency</div>
<div class="abs svc-text" style="left:834px;top:1250px">There are many variations of demo text passed sages of Lorem Ipsum available but the majority.</div>

<h2 class="abs head sec-title" style="top:1347px">From <span>Blog</span></h2>
<div class="abs sec-rule" style="left:591px;top:1382px"></div>

<div class="abs" style="left:0;top:1425px;width:364px;height:229px;background:var(--blog-deep)"></div>
<div class="abs blog-date" style="left:0;width:341px;top:1468px;text-align:right;color:#fff">8 JUNE 2016 &#9638;</div>
<div class="abs head blog-title" style="left:0;width:341px;top:1483px;text-align:right;color:#fff">It Has Nice Clean Design</div>
<div class="abs blog-text" style="left:0;width:341px;top:1528px;text-align:right;color:#fff">Lorem ipsum dolor sit amet, consectetuer adipiscing elit.<br>Aenean commodo ligula eget dolor.</div>
<a class="abs btn blog-btn" style="left:259px;top:1581px">Learn More</a>

<div class="abs" style="left:364px;top:1425px;width:231px;height:229px;background:linear-gradient(180deg,#5a86c4,#c8b49a 60%,#3a9ad0)" role="img" aria-label="Photo of a white villa with a lit swimming pool at dusk"></div>
<div class="abs" style="left:595px;top:1425px;width:230px;height:229px;background:linear-gradient(180deg,#2a3f78,#51607a 55%,#4a3d35)" role="img" aria-label="Photo of a modern house terrace with a fire pit at night"></div>

<div class="abs" style="left:825px;top:1425px;width:375px;height:229px;background:var(--blog-soft)"></div>
<div class="abs blog-date" style="left:852px;top:1468px;color:#fff">8 JUNE 2016 &#9638;</div>
<div class="abs head blog-title" style="left:852px;top:1483px;color:#fff">An Open&nbsp; To Real Estate</div>
<div class="abs blog-text" style="left:852px;top:1528px;color:#fff">Lorem ipsum dolor sit amet, consectetuer adipiscing elit.<br>Aenean commodo ligula eget dolor.</div>
<a class="abs btn blog-btn" style="left:852px;top:1581px">Learn More</a>

<div class="abs" style="left:0;top:1654px;width:364px;height:230px;background:var(--blog-soft)"></div>
<div class="abs blog-date" style="left:0;width:341px;top:1697px;text-align:right;color:#fff">8 JUNE 2016 &#9638;</div>
<div class="abs head blog-title" style="left:0;width:341px;top:1712px;text-align:right;color:#fff">Experienced Real Estate</div>
<div class="abs blog-text" style="left:0;width:341px;top:1757px;text-align:right;color:#fff">Lorem ipsum dolor sit amet, consectetuer adipiscing elit.<br>Aenean commodo ligula eget dolor.</div>
<a class="abs btn blog-btn" style="left:259px;top:1810px">Learn More</a>

<div class="abs" style="left:364px;top:1654px;width:231px;height:230px;background:linear-gradient(180deg,#4f8fd6,#8c8a86 55%,#4f7a3a)" role="img" aria-label="Photo of a suburban stone house with a green lawn"></div>
<div class="abs" style="left:595px;top:1654px;width:230px;height:230px;background:linear-gradient(180deg,#1e2a3e,#9a6a2e 50%,#3a4a58)" role="img" aria-label="Photo of a grand illuminated mansion with pool at night"></div>

<div class="abs" style="left:825px;top:1654px;width:375px;height:230px;background:var(--blog-deep)"></div>
<div class="abs blog-date" style="left:852px;top:1697px;color:#fff">8 JUNE 2016 &#9638;</div>
<div class="abs head blog-title" style="left:852px;top:1712px;color:#fff">Experienced Real Estate</div>
<div class="abs blog-text" style="left:852px;top:1757px;color:#fff">Lorem ipsum dolor sit amet, consectetuer adipiscing elit.<br>Aenean commodo ligula eget dolor.</div>
<a class="abs btn blog-btn" style="left:852px;top:1810px">Learn More</a>

<h2 class="abs head sec-title" style="top:1933px">Contact <span>Us</span></h2>
<div class="abs sec-rule" style="left:591px;top:1968px"></div>
<div class="abs map" role="img" aria-label="Street map of the office neighbourhood"></div>
<div class="abs map-pop">48 HARBOUR LANE , EASTVALE,<br>AUSTRALIA</div>
<div class="abs map-tip"></div>

<footer class="abs footer"></footer>
<h3 class="abs head foot-title" style="left:161px;top:2338px">Our Address</h3>
<div class="abs foot-rule" style="left:161px;top:2363px"></div>
<p class="abs foot-line" style="left:161px;top:2381px;width:270px"><b style="font-size:10px">WE'RE LOOKING FORWARD TO MEETING YOU!!</b><br>Lorem ipsum dolor sit amet, enim putant temp pro, et iuvaret omnesque invenire. Eum case vocibus ex at sed nobis.</p>

<div class="abs info" style="left:161px;top:2453px"><svg viewBox="0 0 14 14" fill="#888"><path d="M7 1a4 4 0 0 1 4 4c0 3-4 8-4 8S3 8 3 5a4 4 0 0 1 4-4z"/><circle cx="7" cy="5" r="1.5" fill="#343434"/></svg>48 Harbour Lane , Eastvale, Australia</div>
<div class="abs info" style="left:161px;top:2478px"><svg viewBox="0 0 14 14" fill="#888"><path d="M3 1l3 3-1.5 1.5a8 8 0 0 0 4 4L10 8l3 3-2 2C6 13 1 8 1 3z"/></svg>+(100) 555 010 4400, +(100) 555 010 4401</div>
<div class="abs info" style="left:161px;top:2502px"><svg viewBox="0 0 14 14" fill="#888"><rect x="1" y="3" width="12" height="8"/><path d="M1 3l6 5 6-5" stroke="#343434" fill="none"/></svg>HELLO@BRIGHTMERE.EXAMPLE</div>
<div class="abs info" style="left:161px;top:2527px"><svg viewBox="0 0 14 14" fill="#888"><path d="M3 1h8L7 7zM3 13h8L7 7z"/></svg>9:00 AM TO 6:00 PM</div>

<h3 class="abs head foot-title" style="left:464px;top:2338px">Get in Touch</h3>
<div class="abs foot-rule" style="left:464px;top:2363px"></div>
<div class="abs ffield" style="left:461px;top:2388px;width:277px;height:32px">Name</div>
<div class="abs ffield" style="left:461px;top:2433px;width:277px;height:32px">Email</div>
<div class="abs ffield" style="left:461px;top:2479px;width:277px;height:32px">Subject</div>
<div class="abs ffield" style="left:763px;top:2388px;width:275px;height:121px">Message...</div>
<a class="abs btn send">Send</a>

<div class="abs bottom">Copyright © 2016 Brightmere - All Rights Reserved</div>

</body>
</html>
```